BAG DESIGN / LAYOUT (cement bag for construction industry)

We need a new bag design as per the powerpoint draft. We are in the construction business and end up on jobsites. The idea is to have a bag on which the operator can easily cross the reference of the product with a marker (1 bag for all our products). Therefore we include the different options on the front of the bag (one list of the different systems we sell, one list of the different colors). We left blank for custom products and colors. Color restriction of the design bag: blue and tones of gray. There could be another color on the general design of the bag. But not more.

Target Market(s)

Contractors

Colors

Designer to choose only greyscale colors for use in the design.

Requirements
Must have
• We must have our logo stand out strongly. Color code possible. The bag can also be determined. We do not wish white too easely dirty. It could be in tones of gray, but you can surprise us with different colors
Nice to have
• A bad that stands out, and that has some character / personality.

```html
<!DOCTYPE html>
<html lang="fr">
<head>
<meta charset="utf-8">
<title>Meridian Concrete – sac 25 kg, plan de découpe</title>
<link href="https://fonts.googleapis.com/css2?family=Lato:wght@400;700;900&display=swap" rel="stylesheet">
<style>
  :root{
    --backdrop:#e4e5e7;
    --sheet:#ffffff;
    --brand-blue:#0d4f8b;
    --brand-grey:#b7b3b4;
    --dieline:#7d8a1e;
    --panel-light:#f4f5f7;
    --panel-mid:#dfe2e6;
    --ink-black:#111111;
    --hazard-red:#e3001b;
  }
  *{margin:0;padding:0;box-sizing:border-box}
  html,body{width:1200px;height:1020px;overflow:hidden;background:var(--backdrop);font-family:'Lato',sans-serif}
  .bag-sheet{position:absolute;left:68px;top:68px;width:1064px;height:884px;background:var(--sheet)}
  .dieline{position:absolute;left:0;top:0;width:1200px;height:1020px}
  .layer{position:absolute;left:0;top:0;width:1200px;height:1020px}
  .abs{position:absolute;white-space:nowrap}
  .brand-name{left:310px;top:433px;width:340px;text-align:center;font-weight:900;font-size:27px;letter-spacing:.5px;color:var(--brand-blue)}
  .brand-name-large{left:800px;top:540px;width:290px;text-align:center;font-weight:900;font-size:30px;line-height:1.15;color:var(--brand-blue)}
  .section-title{font-weight:900;color:var(--brand-blue);font-size:23px}
  .process-tab{position:absolute;top:540px;height:18px;background:var(--brand-blue);color:#fff;font-size:7.5px;line-height:8px;display:flex;align-items:center;justify-content:center;text-align:center;white-space:nowrap}
  .tick-box{position:absolute;top:565px;width:20px;height:15px;border:1.2px solid var(--brand-blue);background:#fff}
  .shade-label{position:absolute;font-weight:700;font-size:11.5px;color:var(--brand-blue)}
  .shade-box{position:absolute;width:60px;height:24px;border:1.4px solid var(--brand-blue);background:#fff}
  .company-block{left:301px;top:803px;font-weight:700;font-size:12.6px;line-height:15.6px;color:var(--brand-blue)}
  .hazard-label{font-weight:700;font-size:9px;color:var(--ink-black)}
  .weight-label{font-weight:700;font-size:12px;color:var(--brand-blue)}
  .weight-box{position:absolute;top:742px;width:29px;height:22px;border:1.4px solid var(--brand-blue);background:#fff}
  .dim{font-family:'Lato',sans-serif;font-size:11px;fill:var(--dieline)}
  .batch-code{left:792px;top:854px;font-size:4px;color:var(--ink-black)}
</style>
</head>
<body>
<div class="bag-sheet"></div>

<svg class="dieline" viewBox="0 0 1200 1020">
  <defs>
    <linearGradient id="panelSheen" x1="0" y1="1" x2="1" y2="0">
      <stop offset="0" stop-color="var(--panel-mid)"/>
      <stop offset=".45" stop-color="var(--panel-light)"/>
      <stop offset=".7" stop-color="#ffffff"/>
      <stop offset="1" stop-color="var(--panel-mid)"/>
    </linearGradient>
    <pattern id="hatch" width="12" height="20" patternUnits="userSpaceOnUse" patternTransform="skewX(45)">
      <line x1="0" y1="0" x2="0" y2="20" stroke="var(--dieline)" stroke-width="1"/>
    </pattern>
  </defs>

  <rect x="104" y="96" width="186" height="784" fill="url(#panelSheen)" role="img" aria-label="Soft diagonal silver sheen across the gusset panels"/>
  <rect x="290" y="96" width="380" height="784" fill="url(#panelSheen)" opacity=".35" role="img" aria-label="Faint silver sheen on the front panel"/>
  <rect x="670" y="96" width="436" height="784" fill="url(#panelSheen)" role="img" aria-label="Soft diagonal silver sheen across the back panel"/>

  <g stroke="var(--dieline)" stroke-width=".8" fill="none">
    <line x1="104" y1="75" x2="1106" y2="75"/>
    <line x1="104" y1="84" x2="1106" y2="84"/>
    <line x1="82" y1="96" x2="82" y2="934"/>
    <line x1="1118" y1="96" x2="1118" y2="880"/>
    <line x1="1118" y1="880" x2="1118" y2="934"/>
    <line x1="480" y1="98" x2="480" y2="314"/>
    <line x1="605" y1="776" x2="605" y2="880"/>
    <line x1="104" y1="80" x2="104" y2="90"/><line x1="126" y1="80" x2="126" y2="90"/>
    <line x1="181" y1="80" x2="181" y2="90"/><line x1="290" y1="80" x2="290" y2="90"/>
    <line x1="670" y1="80" x2="670" y2="90"/><line x1="780" y1="80" x2="780" y2="90"/>
    <line x1="1106" y1="70" x2="1106" y2="90"/>
  </g>
  <text class="dim" x="606" y="78" text-anchor="middle">920</text>
  <text class="dim" x="115" y="88" text-anchor="middle">20</text>
  <text class="dim" x="152" y="88" text-anchor="middle">50</text>
  <text class="dim" x="234" y="88" text-anchor="middle">100</text>
  <text class="dim" x="480" y="88" text-anchor="middle">350</text>
  <text class="dim" x="725" y="88" text-anchor="middle">100</text>
  <text class="dim" x="944" y="88" text-anchor="middle">300</text>
  <text class="dim" transform="translate(86 516) rotate(-90)" text-anchor="middle">770</text>
  <text class="dim" transform="translate(1114 488) rotate(90)" text-anchor="middle">720</text>
  <text class="dim" transform="translate(1114 908) rotate(90)" text-anchor="middle">50</text>
  <text class="dim" transform="translate(476 206) rotate(90)" text-anchor="middle">200</text>
  <text class="dim" transform="translate(601 828) rotate(90)" text-anchor="middle">100</text>

  <g stroke="var(--dieline)" stroke-width="1" fill="none">
    <rect x="126" y="96" width="980" height="784"/>
    <line x1="181" y1="96" x2="181" y2="880"/>
    <line x1="290" y1="96" x2="290" y2="934"/>
    <line x1="670" y1="96" x2="670" y2="934"/>
    <line x1="780" y1="96" x2="780" y2="880"/>
  </g>
  <g stroke="var(--dieline)" stroke-width="1" stroke-dasharray="5 4" fill="none">
    <line x1="104" y1="96" x2="104" y2="934"/>
    <line x1="235" y1="96" x2="235" y2="934"/>
    <line x1="725" y1="96" x2="725" y2="934"/>
    <line x1="1117" y1="96" x2="1117" y2="934"/>
    <line x1="104" y1="934" x2="1117" y2="934"/>
    <polyline points="181,880 235,827 290,880"/>
    <polyline points="670,880 725,827 780,880"/>
  </g>

  <rect x="126" y="804" width="55" height="20" fill="url(#hatch)" stroke="var(--dieline)"/>
  <rect x="780" y="804" width="326" height="20" fill="url(#hatch)" stroke="var(--dieline)"/>
  <rect x="126" y="828" width="44" height="26" fill="none" stroke="var(--dieline)" stroke-width=".8"/>
  <rect x="790" y="824" width="316" height="29" fill="none" stroke="var(--dieline)" stroke-width=".8"/>
  <rect x="108" y="846" width="33" height="6" fill="var(--ink-black)"/>
  <rect x="164" y="842" width="4" height="4" fill="#999"/>
  <rect x="792" y="841" width="4" height="4" fill="#999"/>

  <circle cx="235" cy="776" r="9" fill="none" stroke="#555" stroke-width=".8"/>
  <rect x="222" y="792" width="26" height="7" rx="2" fill="#333"/>

  <g>
    <rect x="587" y="718" width="36" height="36" transform="rotate(45 605 736)" fill="#fff" stroke="#999" stroke-width="3"/>
    <text x="605" y="746" text-anchor="middle" font-family="Lato,sans-serif" font-weight="900" font-size="26" fill="var(--ink-black)">!</text>
  </g>
  <g>
    <rect x="506" y="823" width="24" height="24" transform="rotate(45 518 835)" fill="#fff" stroke="var(--hazard-red)" stroke-width="2"/>
    <text x="518" y="843" text-anchor="middle" font-family="Lato,sans-serif" font-weight="900" font-size="18" fill="var(--ink-black)">!</text>
  </g>
  <rect x="550" y="823" width="24" height="24" transform="rotate(45 562 835)" fill="#fff" stroke="var(--hazard-red)" stroke-width="2" role="img" aria-label="Corrosive hazard pictogram"/>
  <circle cx="480" cy="843" r="3" fill="none" stroke="var(--dieline)" stroke-width=".8"/>
</svg>

<div class="layer">
  <div class="abs brand-name">MERIDIAN CONCRETE</div>

  <div class="abs section-title" style="left:310px;top:504px">PROCEDE</div>
  <div class="process-tab" style="left:310px;width:51px">Colorant<br>Durcisseur</div>
  <div class="process-tab" style="left:369px;width:52px">Sable</div>
  <div class="process-tab" style="left:430px;width:51px">Micro Lisse</div>
  <div class="process-tab" style="left:489px;width:53px">Relief Plus</div>
  <div class="process-tab" style="left:549px;width:45px">Plan'Dal</div>
  <div class="process-tab" style="left:602px;width:46px">Mur Fin</div>
  <div class="tick-box" style="left:325px"></div>
  <div class="tick-box" style="left:385px"></div>
  <div class="tick-box" style="left:445px"></div>
  <div class="tick-box" style="left:505px"></div>
  <div class="tick-box" style="left:562px"></div>
  <div class="tick-box" style="left:615px"></div>

  <div class="abs section-title" style="left:310px;top:597px;font-size:19px">TEINTE</div>
  <div class="shade-label" style="left:310px;top:634px">Pewter</div>
  <div class="shade-label" style="left:310px;top:659px">Acier</div>
  <div class="shade-label" style="left:310px;top:683px">Antractie</div>
  <div class="shade-label" style="left:310px;top:707px">Charbon</div>
  <div class="shade-label" style="left:310px;top:732px">Basalte</div>
  <div class="shade-label" style="left:310px;top:757px">Zinc</div>
  <div class="shade-box" style="left:363px;top:630px"></div>
  <div class="shade-box" style="left:363px;top:655px"></div>
  <div class="shade-box" style="left:363px;top:680px"></div>
  <div class="shade-box" style="left:363px;top:705px"></div>
  <div class="shade-box" style="left:363px;top:730px"></div>
  <div class="shade-box" style="left:363px;top:755px"></div>
  <div class="shade-label" style="left:435px;top:634px">Cappuccino</div>
  <div class="shade-label" style="left:435px;top:659px">Bourgogne</div>
  <div class="shade-label" style="left:435px;top:683px">Sun Buff</div>
  <div class="shade-label" style="left:435px;top:707px">Blanc Cendre</div>
  <div class="shade-label" style="left:435px;top:732px">Rouge Brique</div>
  <div class="shade-label" style="left:435px;top:757px">Terre Cuite</div>
  <div class="shade-box" style="left:509px;top:630px"></div>
  <div class="shade-box" style="left:509px;top:655px"></div>
  <div class="shade-box" style="left:509px;top:680px"></div>
  <div class="shade-box" style="left:509px;top:705px"></div>
  <div class="shade-box" style="left:509px;top:730px"></div>
  <div class="shade-box" style="left:509px;top:755px"></div>

  <div class="abs hazard-label" style="left:590px;top:764px;font-size:6px">Xi - Irritant</div>

  <div class="abs company-block">MERIDIAN CONCRETE SAS<br>18 Chemin des Laves<br>97480 Anse-Claire – Réunion<br>www.meridianconcrete.re</div>
  <div class="abs hazard-label" style="left:503px;top:853px">GHS07</div>
  <div class="abs hazard-label" style="left:547px;top:853px">GHS05</div>

  <div class="abs brand-name-large">MERIDIAN<br>CONCRETE</div>
  <div class="abs section-title" style="left:878px;top:707px;font-size:20px">POIDS</div>
  <div class="abs weight-label" style="left:877px;top:745px">25 KG</div>
  <div class="weight-box" style="left:912px"></div>
  <div class="abs weight-label" style="left:946px;top:745px">20 KG</div>
  <div class="weight-box" style="left:981px"></div>

  <div class="abs batch-code">LOT 0417/02 SAC GRIS</div>
</div>
</body>
</html>
```